Redesign Charity Golf Outing Flyer

We need a redesign of our current golf outing flyer. The charity is in the name of a fallen police officer and the funds help scholarships for future police officers and community projects. I have included the artwork from last year. We brand everything with "The Spark 47" because Gordon's badge number was 182 and he often told people he was "the man". The details on the flyer will need to be editable (we have access to the full Adobe creative suite). While the cause is serious the event itself is fun so feel free to have fun with it.

Target Market(s)

Golfers and people who want to donate.

Industry/Entity Type

Charity

Font styles to use
Sans Serif

Colors
0555a3

Requirements
Must have
• All information included on last years flyer.
Nice to have
• A modern feel.
Should not have
• N/a

```html
<!DOCTYPE html>
<html lang="en">
<head>
<meta charset="utf-8">
<title>Giving on the Green – Golf Scramble Flyer</title>
<link href="https://fonts.googleapis.com/css2?family=Montserrat:wght@400;600;700;800&family=Open+Sans:wght@400;600;700&display=swap" rel="stylesheet">
<style>
:root{
  --blue:#0555a3;
  --green:#3f9c2c;
  --green-dark:#2a6f1c;
  --orange:#ef8a17;
  --ink:#1f2a33;
  --muted:#5b6670;
  --line:#9aa3ab;
  --white:#ffffff;
}
*{margin:0;padding:0;box-sizing:border-box}
html,body{width:849px;height:1200px;overflow:hidden;background:#fff}
.flyer{position:relative;width:849px;height:1200px;overflow:hidden;font-family:"Open Sans",sans-serif;color:var(--ink);background:#fff}
.abs{position:absolute}
.hero{left:0;top:0;width:849px;height:520px;background:
  radial-gradient(circle at 75% 20%,#c9e08a 0,#7fae3c 18%,transparent 40%),
  linear-gradient(180deg,#28401c 0%,#3d6a24 40%,#6fa23a 72%,#ffffff 100%)}
.logo-mark{left:40px;top:28px;width:70px;height:70px;border-radius:50%;background:var(--white)}
.edition{left:130px;top:30px;font-family:"Montserrat",sans-serif;color:var(--white);line-height:1}
.edition .num{font-size:34px;font-weight:800}
.edition .sup{font-size:16px;font-weight:700;vertical-align:top}
.edition .word{display:block;font-size:15px;font-weight:600;margin-top:2px}
.name-band{left:0;top:108px;width:340px;height:44px;background:var(--blue);color:var(--white);font-family:"Montserrat",sans-serif;font-weight:800;font-size:28px;line-height:44px;padding-left:36px;letter-spacing:.5px}
.subtitle{left:36px;top:160px;color:var(--white);font-family:"Montserrat",sans-serif;font-weight:600;font-size:22px}
.ball{left:470px;top:70px;width:250px;height:250px;border-radius:50%;background:radial-gradient(circle at 38% 35%,#ffffff 0,#eef1f2 45%,#b9c2c6 100%)}
.headline{left:36px;top:228px;color:var(--white);font-family:"Montserrat",sans-serif;font-weight:700;font-size:44px;letter-spacing:-.5px}
.tagline{left:36px;top:290px;width:330px;color:var(--white);font-size:16px;font-weight:600;line-height:1.3}
.portrait{left:320px;top:330px;width:170px;height:170px;border-radius:50%;border:6px solid var(--white);background:linear-gradient(160deg,#8a949a,#3a4248);box-shadow:0 3px 10px rgba(0,0,0,.25)}
.tab{left:0;top:393px;width:250px;height:44px;background:var(--green);color:var(--white);font-family:"Montserrat",sans-serif;font-weight:700;font-size:26px;line-height:44px;padding-left:36px}
.date{left:36px;top:448px;font-family:"Montserrat",sans-serif;font-weight:700;font-size:22px;color:var(--ink)}
.times{left:36px;top:484px;font-size:16px;font-weight:600}
.times .row{margin-bottom:4px}
.times .t{color:var(--orange);font-family:"Montserrat",sans-serif;font-weight:700;font-size:18px;margin-right:4px}
.times .note{display:block;font-size:12px;font-weight:400;font-style:italic;color:var(--muted);margin:0 0 6px 0}
.venue{left:36px;top:580px;font-size:14px;line-height:1.4}
.venue strong{font-family:"Montserrat",sans-serif;font-size:18px;color:var(--green-dark)}
.remember{left:530px;top:360px;width:319px;height:80px;background:rgba(5,85,163,.9);color:var(--white);padding:10px 0 0 22px;font-family:"Montserrat",sans-serif}
.remember .a{font-size:16px;font-weight:600}
.remember .b{font-size:26px;font-weight:800;line-height:1.1}
.remember .c{font-size:15px;font-weight:600}
.fee-label{left:552px;top:456px;font-family:"Montserrat",sans-serif;font-weight:700;font-size:22px}
.fees{left:552px;top:490px;display:flex;gap:0}
.fee{width:120px;height:56px;display:flex;align-items:center;gap:6px;padding-left:10px}
.fee + .fee{border-left:2px solid var(--line)}
.fee .amt{font-family:"Montserrat",sans-serif;font-weight:800;font-size:38px;line-height:1}
.fee .amt sup{font-size:18px;vertical-align:top}
.fee .per{font-size:14px;line-height:1.1}
.includes{left:552px;top:552px;font-size:12.5px;line-height:1.35;color:var(--muted)}
.register{left:500px;top:603px;width:349px;height:60px;background:var(--green);color:var(--white);padding:6px 0 0 30px;font-family:"Montserrat",sans-serif}
.register .a{font-size:14px;font-weight:600}
.register .b{font-size:20px;font-weight:800}
.form{left:0;top:676px;width:500px;height:430px;border-top:3px solid var(--blue);padding:16px 36px 0}
.form h3{font-family:"Montserrat",sans-serif;font-size:18px;color:var(--blue);margin-bottom:10px}
.field{display:flex;align-items:flex-end;height:34px;font-size:13px;font-weight:600}
.field .line{flex:1;border-bottom:1px dotted var(--line);margin-left:6px;height:14px}
.field .gap{width:10px}
.sponsor{left:530px;top:680px;width:300px}
.sponsor .q{font-family:"Montserrat",sans-serif;font-weight:700;font-size:15px}
.sponsor .big{font-family:"Montserrat",sans-serif;font-weight:800;font-size:24px;color:var(--blue);margin-bottom:16px}
.sponsor .lbl{font-size:13px;font-weight:700}
.sponsor .hint{font-size:11px;color:var(--muted)}
.sponsor .box{border-bottom:1px dotted var(--line);height:40px;margin-bottom:14px}
.contact{left:530px;top:940px;width:290px;border-left:3px solid var(--green);padding:6px 0 6px 16px;font-size:13px;line-height:1.4}
.contact .h{font-weight:700;color:var(--muted)}
.contact .n{font-family:"Montserrat",sans-serif;font-weight:700;font-size:15px}
.footer{left:0;top:1110px;width:849px;height:90px;background:var(--green);color:var(--white);padding:16px 36px}
.footer .d{font-family:"Montserrat",sans-serif;font-weight:700;font-size:18px}
.footer .m{font-size:13px;margin-top:4px}
.footer .m strong{font-style:italic}
</style>
</head>
<body>
<main class="flyer">
  <div class="abs hero" role="img" aria-label="Photo of a golf course green with soft blurred background"></div>

  <div class="abs logo-mark" aria-hidden="true"></div>
  <div class="abs edition"><span class="num">3</span><span class="sup">rd</span><span class="word">Annual</span></div>
  <div class="abs name-band">GORDON D. HALE</div>
  <div class="abs subtitle">Memorial &amp; Scholarship</div>

  <div class="abs ball" role="img" aria-label="Photo of a golf ball on a tee"></div>

  <h1 class="abs headline">Giving on the Green:</h1>
  <p class="abs tagline">A Charity Golf Outing for "THE SPARK 47" Benefitting future police officers and community projects</p>

  <div class="abs portrait" role="img" aria-label="Portrait photo of officer Gordon D. Hale"></div>

  <div class="abs tab">Golf Scramble</div>
  <div class="abs date">Saturday-August 00, 2016</div>
  <div class="abs times">
    <div class="row"><span class="t">09.00AM</span> – Registration</div>
    <span class="note">(Day of scramble registrations are welcome)</span>
    <div class="row"><span class="t">10.00AM</span> – Shotgun Start</div>
  </div>
  <div class="abs venue"><strong>Cedar Ridge Golf Course</strong><br>3140 Harmon Avenue Rd, Mansfield, OH 44903<br>Ph : (419) 555-0192</div>

  <div class="abs remember"><div class="a">Remebering</div><div class="b">"THE SPARK"</div><div class="c">Gordon D. Hale</div></div>

  <div class="abs fee-label">Entry Fee :</div>
  <div class="abs fees">
    <div class="fee"><span class="amt"><sup>$</sup>55</span><span class="per">Per<br>Person</span></div>
    <div class="fee"><span class="amt"><sup>$</sup>220</span><span class="per">Per<br>Team</span></div>
  </div>
  <div class="abs includes">Includes: Green Fees,<br>cart and dinner</div>

  <div class="abs register"><div class="a">Register below or online at:</div><div class="b">www.47golf.eventpage.com</div></div>

  <section class="abs form">
    <h3>Team Captain Information:</h3>
    <div class="field">Captain's Name:<span class="line"></span></div>
    <div class="field">Address:<span class="line"></span></div>
    <div class="field">City:<span class="line"></span><span class="gap"></span>State:<span class="line"></span><span class="gap"></span>Zip:<span class="line"></span></div>
    <div class="field">Captain's Phone:<span class="line"></span></div>
    <div class="field">Captain's Mail:<span class="line"></span></div>
    <div class="field">Player#2 Name:<span class="line"></span></div>
    <div class="field">Player#3 Name:<span class="line"></span></div>
    <div class="field">Player#4 Name:<span class="line"></span></div>
  </section>

  <section class="abs sponsor">
    <div class="q">Can't Make it or Don't Golf?</div>
    <div class="big">Sponsor a hole/tee:</div>
    <div class="lbl">Name/Business</div>
    <div class="hint">(Attach business card if possible)</div>
    <div class="box"></div>
    <div class="lbl">Donation Amount:</div>
    <div class="box"></div>
  </section>

  <div class="abs contact">
    <div class="h">Any Questions Contact:</div>
    <div class="n">Dale Morrow</div>
    1420 Maple Crest Lane<br>Ontario, OH 44906<br>(419) 555-0148
  </div>

  <footer class="abs footer">
    <div class="d">Mail-in Deadline: August 1, 2016</div>
    <div class="m">Mail this completed form with check(s) made payable to: <strong>"The Officer Gordon D. Hale Memorial Scholarship Fund"</strong></div>
  </footer>
</main>
</body>
</html>
```